Bref créative
RVM Ltd stationary set
letterhead, business cards, envelopes
I need single sided standard sized Business Card [3.5" x 2"]
Designer's choice
Professional
Martin K. Dobbs
Registered Patent Attorney
82 E. Parkhill Street
Suite 4785
Chicago, IL 60417
martindobbs@claimwisp.com
www.claimwisp.com
A version of the "old" letterhead can be downloaded here: https://claimwisp.filevault-example.net/shared/q8tr2m4vbnxwpla7c3dk
RVM logo (ai format)

```html
<!DOCTYPE html>
<html lang="en">
<head>
<meta charset="utf-8">
<title>RVM Ltd Stationery Set</title>
<link rel="stylesheet" href="https://fonts.googleapis.com/css2?family=Cinzel:wght@500&family=Open+Sans:wght@400;600&display=swap">
<style>
  :root {
    --backdrop: #a6a6a8;
    --paper: #ffffff;
    --brand-blue: #2d5aa6;
    --ink: #3a3a3a;
    --muted: #7a7a7a;
    --fold-line: #cfcfd4;
  }
  * { margin: 0; padding: 0; box-sizing: border-box; }
  html, body { width: 1200px; height: 684px; overflow: hidden; }
  body {
    background: var(--backdrop);
    position: relative;
    font-family: "Open Sans", Arial, sans-serif;
    color: var(--ink);
  }
  .sheet {
    position: absolute;
    background: var(--paper);
    box-shadow: 0 1px 3px rgba(0,0,0,.25);
    overflow: hidden;
  }
  .band { position: absolute; left: 0; right: 0; background: var(--brand-blue); }
  .band-top { top: 0; }
  .band-bottom {
    bottom: 0;
    color: var(--paper);
    font-size: 6px;
    display: flex; align-items: center; justify-content: center;
    letter-spacing: .3px;
  }
  .brand {
    position: absolute; left: 0; right: 0;
    display: flex; flex-direction: column; align-items: center;
  }
  .brand-mark { display: flex; align-items: center; gap: 3px; }
  .brand-square { background: var(--brand-blue); }
  .brand-initials {
    font-family: "Cinzel", Georgia, serif; font-weight: 500;
    color: var(--brand-blue);
  }
  .brand-name {
    font-family: "Cinzel", Georgia, serif; font-weight: 500;
    color: var(--brand-blue); letter-spacing: 1px; margin-top: 3px;
  }
  .brand-tagline { color: var(--muted); letter-spacing: .6px; margin-top: 1px; }
  .contact-line {
    position: absolute; left: 0; right: 0; text-align: center;
    font-size: 5px; color: var(--ink); letter-spacing: .2px;
  }
  .contact-line b { color: var(--brand-blue); font-weight: 600; }

  /* Letterhead */
  .letterhead { left: 192px; top: 12px; width: 444px; height: 648px; }
  .letterhead .band-top { height: 17px; }
  .letterhead .band-bottom { height: 19px; }
  .letterhead .brand { top: 30px; }
  .letterhead .brand-square { width: 14px; height: 14px; }
  .letterhead .brand-initials { font-size: 13px; }
  .letterhead .brand-name { font-size: 8px; }
  .letterhead .brand-tagline { font-size: 4px; }
  .letterhead .contact-line { top: 585px; }

  /* Business card */
  .business-card { left: 34px; top: 288px; width: 151px; height: 134px; }
  .business-card .band-top { height: 5px; }
  .business-card .band-bottom { height: 14px; font-size: 5px; }
  .card-identity {
    position: absolute; left: 0; top: 44px; width: 78px;
    display: flex; flex-direction: column; align-items: center;
  }
  .card-identity .brand-square { width: 11px; height: 11px; }
  .card-identity .brand-initials { font-size: 10px; }
  .card-identity .brand-name { font-size: 6px; letter-spacing: .5px; }
  .card-identity .brand-tagline { font-size: 3px; }
  .card-divider { position: absolute; left: 79px; top: 22px; width: 1px; height: 84px; background: var(--fold-line); }
  .card-details { position: absolute; left: 85px; top: 24px; font-size: 4px; line-height: 6px; }
  .card-details .person { font-size: 5px; font-weight: 600; color: var(--brand-blue); }
  .card-details .title { color: var(--muted); margin-bottom: 8px; }

  /* Envelope back */
  .envelope-back { left: 655px; top: 12px; width: 526px; height: 324px; }
  .envelope-back svg { position: absolute; inset: 0; }
  .envelope-back .brand { top: 48px; }
  .envelope-back .brand-square { width: 22px; height: 22px; }
  .envelope-back .brand-initials { font-size: 26px; }

  /* Envelope front */
  .envelope-front { left: 655px; top: 365px; width: 526px; height: 223px; }
  .envelope-front .band-top { height: 19px; }
  .envelope-front .band-bottom { height: 19px; }
  .envelope-front .brand { top: 36px; }
  .envelope-front .brand-square { width: 12px; height: 12px; }
  .envelope-front .brand-initials { font-size: 12px; }
  .envelope-front .brand-name { font-size: 7px; }
  .envelope-front .brand-tagline { font-size: 4px; }
  .envelope-front .contact-line { top: 183px; }
</style>
</head>
<body>

<section class="sheet letterhead" aria-label="Letterhead">
  <div class="band band-top"></div>
  <div class="brand">
    <div class="brand-mark"><span class="brand-square"></span><span class="brand-initials">RVM</span></div>
    <div class="brand-name">RVM LTD.</div>
    <div class="brand-tagline">REGISTERED PATENT ATTORNEY</div>
  </div>
  <p class="contact-line"><b>T:</b> (312) 555-0142 &nbsp;|&nbsp; <b>F:</b> (312) 555-0143 &nbsp;|&nbsp; <b>E:</b> martindobbs@claimwisp.com &nbsp;|&nbsp; <b>A:</b> 82 E. Parkhill Street, Suite 4785, Chicago, IL 60417</p>
  <div class="band band-bottom">www.claimwisp.com</div>
</section>

<section class="sheet business-card" aria-label="Business card">
  <div class="band band-top"></div>
  <div class="card-identity">
    <div class="brand-mark"><span class="brand-square"></span><span class="brand-initials">RVM</span></div>
    <div class="brand-name">RVM LTD.</div>
    <div class="brand-tagline">REGISTERED PATENT ATTORNEY</div>
  </div>
  <div class="card-divider"></div>
  <div class="card-details">
    <div class="person">Martin K. Dobbs</div>
    <div class="title">Registered Patent Attorney</div>
    <div>T: (312) 555-0142</div>
    <div>F: (312) 555-0143</div>
    <div>E: martindobbs@claimwisp.com</div>
    <div>A: 82 E. Parkhill Street</div>
    <div>&nbsp;&nbsp;&nbsp;&nbsp;Suite 4785</div>
    <div>&nbsp;&nbsp;&nbsp;&nbsp;Chicago, IL 60417</div>
  </div>
  <div class="band band-bottom">www.claimwisp.com</div>
</section>

<section class="sheet envelope-back" aria-label="Envelope back">
  <svg width="526" height="324" viewBox="0 0 526 324">
    <path d="M0 0 L40 200 Q263 250 486 200 L526 0" fill="none" stroke="var(--fold-line)" stroke-width="1"/>
  </svg>
  <div class="brand">
    <div class="brand-mark"><span class="brand-square"></span><span class="brand-initials">RVM</span></div>
  </div>
</section>

<section class="sheet envelope-front" aria-label="Envelope front">
  <div class="band band-top"></div>
  <div class="brand">
    <div class="brand-mark"><span class="brand-square"></span><span class="brand-initials">RVM</span></div>
    <div class="brand-name">RVM LTD.</div>
    <div class="brand-tagline">REGISTERED PATENT ATTORNEY</div>
  </div>
  <p class="contact-line"><b>T:</b> (312) 555-0142 &nbsp;|&nbsp; <b>F:</b> (312) 555-0143 &nbsp;|&nbsp; <b>E:</b> martindobbs@claimwisp.com &nbsp;|&nbsp; <b>A:</b> 82 E. Parkhill Street, Suite 4785, Chicago, IL 60417</p>
  <div class="band band-bottom">www.claimwisp.com</div>
</section>

</body>
</html>
```